Residential Construction Business - Site Signage

I need a design made for a site fence banner. We have a logo and branding so the design would need to be aligned with this. It would need to be made to specific size ratio so that it can be sent to the maker for production.
ratio : 4600 wide x 1700 high
The design should feature our website and also the slogan
"don't move, re-imagine"

Target Market(s)

potential clients

Industry/Entity Type

construction

Font styles to use
Other font styles liked:
• to match branding

Colors
0054AA
0677BA
7BADD7
CADEEF
E8F1F8

Requirements
Must have
• www.velmbuild.com.au Majority of the sign is our brand logo
Nice to have
• Majority of the sign is our brand logo
Should not have
• colors and themes that arent brand relevant

```html
<!DOCTYPE html>
<html lang="en">
<head>
<meta charset="utf-8">
<title>Velm Build – Site Fence Banner</title>
<link rel="stylesheet" href="https://fonts.googleapis.com/css2?family=Montserrat:wght@500;600&family=Oswald:wght@300;400&display=swap">
<style>
  :root {
    --brand-navy: #043c5c;
    --band-charcoal: #3f3f41;
    --text-dark: #3a3a3c;
    --paper: #ffffff;
    --backdrop: #e9e9e9;
    --rule: #2b2b2d;
  }
  html, body {
    margin: 0;
    padding: 0;
    width: 1200px;
    height: 600px;
    overflow: hidden;
    background: var(--backdrop);
  }
  .canvas {
    position: relative;
    width: 1200px;
    height: 600px;
  }
  .fence-banner {
    position: absolute;
    left: 20px;
    top: 85px;
    width: 1160px;
    height: 430px;
    display: block;
  }
  .banner-paper { fill: var(--paper); }
  .brand-chevron { fill: var(--brand-navy); }
  .contact-band { fill: var(--band-charcoal); }
  .hanging-rule { stroke: var(--rule); stroke-width: 1.2; }
  .brand-name {
    font-family: "Montserrat", sans-serif;
    font-weight: 600;
    font-size: 38px;
    letter-spacing: 14px;
    fill: var(--brand-navy);
  }
  .slogan {
    font-family: "Oswald", sans-serif;
    text-anchor: end;
  }
  .slogan-line-one { font-size: 60px; }
  .slogan-line-two { font-size: 104px; }
  .slogan-muted { font-weight: 300; fill: var(--text-dark); }
  .slogan-accent { font-weight: 400; fill: var(--brand-navy); }
  .slogan-line-two .slogan-muted { font-weight: 400; }
  .contact-phone {
    font-family: "Montserrat", sans-serif;
    font-weight: 500;
    font-size: 18px;
    letter-spacing: 3px;
    fill: var(--text-dark);
  }
  .contact-web {
    font-family: "Montserrat", sans-serif;
    font-weight: 500;
    font-size: 18px;
    letter-spacing: 3px;
    fill: var(--paper);
    text-anchor: end;
  }
</style>
</head>
<body>
<main class="canvas">
  <svg class="fence-banner" viewBox="0 0 1080 400" preserveAspectRatio="none" aria-label="Velm Build site fence banner">
    <rect class="banner-paper" x="0" y="0" width="1080" height="400"/>
    <polygon class="brand-chevron" points="0,0 385,0 270,158 395,289 0,289"/>
    <polygon class="contact-band" points="415,310 1080,310 1080,400 495,400"/>
    <line class="hanging-rule" x1="812" y1="0" x2="812" y2="82"/>

    <text class="brand-name" x="306" y="157">VELM BUILD</text>

    <text class="slogan slogan-line-one" x="1025" y="157"><tspan class="slogan-muted">don't </tspan><tspan class="slogan-accent">move</tspan></text>
    <text class="slogan slogan-line-two" x="1025" y="253"><tspan class="slogan-muted">re-</tspan><tspan class="slogan-accent">imagine</tspan></text>

    <text class="contact-phone" x="100" y="350">(+61) 455 318 920</text>
    <text class="contact-web" x="1025" y="350">WWW.VELMBUILD.COM.AU</text>
  </svg>
</main>
</body>
</html>
```